Real Estate Company Needs Business Card Designed

We need a business card design for a new real estate company based in Campbell, CA (Silicon Valley). We plan to improve the residential real estate industry by using technology to improve customer experience. We would like to see designs that use a black background. The final design should communicate sophistication and customer service, as well as stability and technology.

Industry/Entity Type

Real Estate

Requirements
Must have
• Black background

```html
<!DOCTYPE html>
<html lang="en">
<head>
<meta charset="utf-8">
<title>Velmont Real Estate Services – Business Card</title>
<link rel="stylesheet" href="https://fonts.googleapis.com/css2?family=Michroma&display=swap">
<style>
  :root {
    --page-bg: #1d1d1f;
    --card-black: #050607;
    --facet-dark: #0d1014;
    --facet-mid: #161a20;
    --facet-light: #1f242b;
    --divider: #2c5d9c;
    --white: #f4f6f8;
    --blue: #3f7fd6;
    --blue-soft: #4b86d8;
  }
  * { margin: 0; padding: 0; box-sizing: border-box; }
  html, body {
    width: 1200px;
    height: 1082px;
    overflow: hidden;
    background: var(--page-bg);
  }
  body {
    position: relative;
    font-family: "Michroma", "Eurostile", sans-serif;
  }
  .business-card {
    position: absolute;
    left: 100px;
    top: 255px;
    width: 1000px;
    height: 571px;
    background: var(--card-black);
    overflow: hidden;
    box-shadow: 0 30px 60px rgba(0,0,0,0.55);
  }
  .card-facets {
    position: absolute;
    inset: 0;
    width: 100%;
    height: 100%;
  }
  .card-divider {
    position: absolute;
    left: 530px;
    top: 0;
    width: 2px;
    height: 100%;
    background: var(--divider);
    opacity: 0.7;
  }
  .identity {
    position: absolute;
    right: 500px;
    top: 200px;
    text-align: right;
  }
  .person-name {
    color: var(--white);
    font-size: 34px;
    letter-spacing: 1px;
    line-height: 1.2;
    text-shadow: 0 0 1px var(--white);
  }
  .person-title {
    color: var(--blue);
    font-size: 18px;
    letter-spacing: 3px;
    margin-top: 6px;
    padding-top: 6px;
    border-top: 1px solid var(--divider);
    display: inline-block;
  }
  .brand-block {
    position: absolute;
    right: 500px;
    top: 345px;
    text-align: right;
  }
  .brand-name {
    color: var(--white);
    font-size: 58px;
    letter-spacing: 2px;
    line-height: 1;
  }
  .brand-tagline {
    color: var(--blue);
    font-size: 14px;
    letter-spacing: 4px;
    margin-top: 12px;
    padding-top: 8px;
    border-top: 1px solid var(--divider);
  }
  .contact-panel {
    position: absolute;
    left: 590px;
    right: 60px;
    top: 70px;
    text-align: right;
  }
  .brand-mark {
    display: flex;
    align-items: center;
    justify-content: center;
    gap: 12px;
    margin-bottom: 60px;
  }
  .brand-mark-square {
    width: 22px;
    height: 22px;
    background: var(--blue);
  }
  .brand-mark-name {
    color: var(--white);
    font-size: 30px;
    letter-spacing: 3px;
  }
  .address {
    color: var(--white);
    font-size: 17px;
    letter-spacing: 2px;
    line-height: 1.75;
  }
  .address .zip { color: var(--blue-soft); }
  .contact-lines {
    margin-top: 40px;
    font-size: 15px;
    letter-spacing: 2px;
    line-height: 1.9;
    color: var(--white);
  }
  .contact-lines .accent { color: var(--blue-soft); }
</style>
</head>
<body>
  <article class="business-card">
    <svg class="card-facets" viewBox="0 0 1000 571" preserveAspectRatio="none" aria-hidden="true">
      <polygon points="0,0 300,0 530,200 530,571 0,571" fill="var(--facet-dark)"/>
      <polygon points="0,120 240,0 300,0 0,330" fill="var(--facet-mid)"/>
      <polygon points="0,330 300,0 530,200 530,571 200,571" fill="var(--facet-light)" opacity="0.55"/>
      <polygon points="200,571 530,300 530,571" fill="var(--facet-dark)"/>
    </svg>
    <div class="card-divider"></div>

    <header class="identity">
      <h1 class="person-name">DANIEL REYES</h1>
      <p class="person-title">VICE PRESIDENT</p>
    </header>

    <div class="brand-block">
      <p class="brand-name">VELMONT</p>
      <p class="brand-tagline">REAL ESTATE SERVICES</p>
    </div>

    <section class="contact-panel">
      <div class="brand-mark">
        <span class="brand-mark-square"></span>
        <span class="brand-mark-name">VELMONT</span>
      </div>
      <p class="address">
        2240 W. Harlow Ave.,<br>
        6th Floor, Campbell<br>
        <span class="zip">95010</span>
      </p>
      <p class="contact-lines">
        danielreyes<span class="accent">@velmont.com</span><br>
        <span class="accent">+1</span> (408) 555-0178<br>
        <span class="accent">www.velmont.com</span>
      </p>
    </section>
  </article>
</body>
</html>
```